Jumbo direct mailing Postcard design

I need a design for an oversized postcard mailer that will be marketing a ballroom dance studio located in Cary, NC. We are an Vernon Callow franchised dance studio and considered the gold standard for ballroom dance lessons. Our instructors our certified and top quality. The size of the postcard is 8.5" x 5.5" and will be full color. Our website is carystepwell-example.com
This will be marketed to men and women. Average age is 30-60. Mostly females apply, but some males, see sliders.
We want an eye catching postcard to get people to call. We are offering a free dance lesson to people that either call or go to our website and fill out the form.
Some ideas we had for headlines are:
-
Bored in Cary? Looking for something new to try? Learn how to
-Spice up date night
-Meet new people at our dance parties
-Lose weight
-Gain confidence while learning a valuable social skill
-
We can discuss headlines and text in feedback discussion.
I will be uploading some creative assets you can use for this project, but are not required to be used at all. They are not the best looking creatives.
The final design should communicate a fun valuable social activity and skill to the reader and showing how our school is the best quality in the market. Using gold and black colors could accompany that.
Target Market(s)
men/women luxury market, age 30-60. affluent individuals
Industry/Entity Type
Dance Studio
Look and feel
Each slider illustrates characteristics of the customer's brand and the style your logo design should communicate.

```html
<!DOCTYPE html>
<html lang="en">
<head>
<meta charset="utf-8">
<title>Vernon Callow – Cary Postcard Front</title>
<link href="https://fonts.googleapis.com/css2?family=Caladea&family=Tinos&display=swap" rel="stylesheet">
<style>
  :root {
    --backdrop: #e4e4e4;
    --card-black: #030303;
    --arc-grey: #1c1c1c;
    --arc-edge: #4a4a4a;
    --gold: #c8912c;
    --gold-soft: #c99a3a;
    --amber-deep: #5a3208;
    --white: #ffffff;
  }
  * { margin: 0; padding: 0; box-sizing: border-box; }
  html, body {
    width: 1200px;
    height: 900px;
    overflow: hidden;
  }
  body {
    background: var(--backdrop);
    position: relative;
  }
  .postcard {
    position: absolute;
    left: 39px;
    top: 88px;
    width: 1121px;
    height: 727px;
    background: var(--card-black);
    overflow: hidden;
  }
  .floral-area {
    position: absolute;
    left: 0;
    top: 0;
    width: 560px;
    height: 100%;
    background:
      radial-gradient(ellipse at 25% 30%, rgba(214,140,40,0.55) 0%, rgba(120,66,12,0.35) 35%, transparent 70%),
      radial-gradient(ellipse at 20% 80%, rgba(180,110,30,0.45) 0%, rgba(90,50,8,0.3) 40%, transparent 75%),
      linear-gradient(90deg, var(--amber-deep) 0%, rgba(60,32,6,0.8) 45%, rgba(3,3,3,0) 100%);
  }
  .corner-arc {
    position: absolute;
    right: 0;
    top: 0;
    width: 580px;
    height: 220px;
  }
  .brand {
    position: absolute;
    left: 711px;
    top: 52px;
    color: var(--white);
    font-family: "Caladea", serif;
    display: flex;
    align-items: center;
    gap: 12px;
  }
  .brand-mark {
    width: 14px;
    height: 14px;
    border-radius: 50%;
    background: var(--white);
  }
  .brand-name {
    font-size: 36px;
    font-weight: 700;
    letter-spacing: 0.5px;
  }
  .brand-tagline {
    position: absolute;
    left: 737px;
    top: 98px;
    color: var(--white);
    font-family: "Caladea", serif;
    font-size: 14px;
    letter-spacing: 1px;
  }
  .headline {
    position: absolute;
    left: 432px;
    top: 243px;
    color: var(--white);
    font-family: "Caladea", serif;
    font-size: 76px;
    font-weight: 400;
    line-height: 1;
  }
  .subhead {
    position: absolute;
    left: 432px;
    top: 322px;
    color: var(--gold);
    font-family: "Caladea", serif;
    font-size: 38px;
    font-weight: 400;
    line-height: 1;
  }
  .benefits-title {
    position: absolute;
    left: 670px;
    top: 405px;
    color: var(--white);
    font-family: "Tinos", serif;
    font-size: 31px;
    font-weight: 400;
    line-height: 1;
  }
  .benefits {
    position: absolute;
    left: 670px;
    top: 450px;
    list-style: none;
    color: var(--gold-soft);
    font-family: "Tinos", serif;
    font-size: 22px;
    line-height: 35px;
  }
  .benefits li {
    position: relative;
    padding-left: 25px;
  }
  .benefits li::before {
    content: "";
    position: absolute;
    left: 2px;
    top: 12px;
    width: 11px;
    height: 11px;
    border-radius: 50%;
    background: radial-gradient(circle at 35% 35%, #f0cf7a 0%, var(--gold) 60%, #7a5212 100%);
  }
</style>
</head>
<body>
  <main class="postcard">
    <div class="floral-area" role="img" aria-label="Gold baroque floral swirl pattern with glowing sparkles on black"></div>

    <svg class="corner-arc" viewBox="0 0 580 220" aria-hidden="true">
      <defs>
        <linearGradient id="arcFill" x1="0" y1="0" x2="1" y2="1">
          <stop offset="0" stop-color="#262626"/>
          <stop offset="1" stop-color="#0c0c0c"/>
        </linearGradient>
      </defs>
      <path d="M0 0 Q 120 150 580 150 L580 0 Z" fill="url(#arcFill)"/>
      <path d="M110 120 Q 300 230 580 160 L580 172 Q 300 245 110 120 Z" fill="var(--arc-grey)"/>
      <path d="M0 0 Q 120 150 580 150" fill="none" stroke="var(--arc-edge)" stroke-width="1.5"/>
    </svg>

    <div class="brand">
      <span class="brand-mark"></span>
      <span class="brand-name">Vernon Callow</span>
    </div>
    <p class="brand-tagline">Franchised Dance Studios</p>

    <h1 class="headline">Bored in Cary?</h1>
    <p class="subhead">Looking for something new to try?</p>

    <h2 class="benefits-title">LEARN HOW TO</h2>
    <ul class="benefits">
      <li>Spice up date night</li>
      <li>Meet new people at our<br>dance parties</li>
      <li>Lose weight</li>
      <li>Gain confidence while learning<br>a valuable social skill</li>
    </ul>
  </main>
</body>
</html>
```